Brava Set CEO and Partners Business Card

We need a fresh, fun, simple and clean business card design....we would like a template where we can add a name and title (as well as specific email addresses). We are open to different looks (full logo on one side and a small logo on the company info side, or our logo is in the background but faint on one side but full on the other, or something else cool :-) ). Our colors are in our logo: blue, black and white...however we are not opposed to the use of other colors if it works. We build sets, make props and a host of other things for the film and television industry...our card should reflect creativity, style and professionalism.

A white background would be preferred.

I would like to see an option with Facebook and Instagram icons.

Facebook- facebook.com/bravasetny
Instagram- brava_set

Our website is bravaset-example.com.

Brava Set, Inc.
418 Corvell Avenue, Unit 9
North Hollywood, California 91602
555.210.4873 | tel
555.210.6692 | fax
www.BravaSet-example.com

Sample Name and Title #1:

Peter Halvik
CEO / Co-Owner
555.210.4873 | tel
555.210.6692 | fax
peter@bravaset-example.com
www.BravaSet-example.com

Target Market(s)

Marketing Professionals, Production Designers, Interior Designers, Film Producers, Directors, Art Directors, Event Directors

Industry/Entity Type

Entertainment Industry

Contact Information for Business Card

Peter Halvik
CEO / Co-Owner
555.210.4873 | tel
555.210.6692 | fax
peter@bravaset-example.com
www.BravaSet-example.com

Font styles to use
Sans Serif

Colors
33a6d7
ffffff
1b1b1b

Requirements
Must have
• Logo, All Contact Info, White Background. Symmetry.
Nice to have
• Facebook and Instagram icons with addresses
• Facebook- facebook.com/bravasetny
• Instagram- brava_set

```html
<!DOCTYPE html>
<html lang="en">
<head>
<meta charset="utf-8">
<title>Brava Set — Business Card</title>
<link rel="stylesheet" href="https://fonts.googleapis.com/css2?family=Open+Sans:wght@300;400;800&display=swap">
<style>
  :root {
    --brand-blue: #33a6d7;
    --ink: #1b1b1b;
    --paper: #ffffff;
    --backdrop: #ebedef;
    --muted: #3a3a3a;
  }
  * { box-sizing: border-box; margin: 0; padding: 0; }
  html, body { width: 1200px; height: 1200px; overflow: hidden; }
  body {
    background: var(--backdrop);
    font-family: "Open Sans", Arial, sans-serif;
    color: var(--ink);
    display: flex;
    flex-direction: column;
    align-items: center;
    justify-content: center;
    gap: 60px;
  }
  .card {
    width: 700px;
    height: 400px;
    background: var(--paper);
    position: relative;
    box-shadow: 0 2px 10px rgba(0,0,0,.12);
    overflow: hidden;
  }
  .wordmark {
    font-weight: 800;
    color: var(--ink);
    letter-spacing: 1px;
    display: flex;
    align-items: center;
    gap: 14px;
    white-space: nowrap;
  }
  .wordmark__dot {
    width: 18px; height: 18px;
    background: var(--brand-blue);
  }
  /* Front: contact side */
  .card--front .wordmark {
    position: absolute;
    left: 50px; top: 130px;
    font-size: 50px;
  }
  .divider {
    position: absolute;
    left: 420px; top: 36px;
    width: 1px; height: 250px;
    background: linear-gradient(to bottom, rgba(51,166,215,0), var(--brand-blue) 55%, rgba(51,166,215,0));
  }
  .person {
    position: absolute;
    right: 40px; top: 40px;
    text-align: right;
  }
  .person__name { font-weight: 300; font-size: 27px; line-height: 1.1; }
  .person__title { font-weight: 400; font-size: 13px; margin-top: 4px; }
  .contact {
    position: absolute;
    right: 40px; top: 160px;
    display: flex;
    gap: 10px;
    align-items: flex-start;
  }
  .contact__lines {
    list-style: none;
    text-align: right;
    font-size: 14px;
    font-weight: 400;
    line-height: 24px;
    color: var(--muted);
  }
  .contact__icons {
    display: flex;
    flex-direction: column;
    gap: 6px;
    padding-top: 3px;
  }
  .icon {
    width: 18px; height: 18px;
    background: var(--brand-blue);
    display: block;
  }
  .address-band {
    position: absolute;
    left: 0; right: 0; bottom: 0;
    height: 64px;
    background: var(--brand-blue);
    display: flex;
    align-items: center;
    justify-content: center;
    font-size: 15px;
    color: var(--ink);
    font-weight: 400;
  }
  /* Back: logo side */
  .card--back {
    display: flex;
    align-items: center;
    justify-content: center;
    background: radial-gradient(circle at 50% 50%, #ffffff 40%, #f1f1f1 100%);
  }
  .card--back .wordmark { font-size: 72px; gap: 20px; }
  .card--back .wordmark__dot { width: 26px; height: 26px; }
</style>
</head>
<body>
  <section class="card card--front" aria-label="Business card, contact side">
    <div class="wordmark"><span class="wordmark__text">Brava Set</span><span class="wordmark__dot"></span></div>
    <div class="divider"></div>
    <div class="person">
      <p class="person__name">Peter Halvik</p>
      <p class="person__title">CEO / Co-Owner</p>
    </div>
    <div class="contact">
      <ul class="contact__lines">
        <li>555.210.4873</li>
        <li>555.210.6692</li>
        <li>www.BravaSet-example.com</li>
        <li>peter@bravaset-example.com</li>
      </ul>
      <div class="contact__icons">
        <svg class="icon" viewBox="0 0 18 18" aria-label="phone"><rect width="18" height="18" fill="#33a6d7"/><path d="M5 4h3l1 3-2 1a7 7 0 0 0 3 3l1-2 3 1v3c-5 0-9-4-9-9z" fill="#fff"/></svg>
        <svg class="icon" viewBox="0 0 18 18" aria-label="fax"><rect width="18" height="18" fill="#33a6d7"/><rect x="6" y="3" width="6" height="4" fill="#fff"/><rect x="4" y="8" width="10" height="5" fill="#fff"/><rect x="6" y="11" width="6" height="4" fill="#fff" stroke="#33a6d7"/></svg>
        <svg class="icon" viewBox="0 0 18 18" aria-label="website"><rect width="18" height="18" fill="#33a6d7"/><circle cx="9" cy="9" r="5" fill="none" stroke="#fff" stroke-width="1.4"/><path d="M4 9h10M9 4c-2.5 3-2.5 7 0 10M9 4c2.5 3 2.5 7 0 10" fill="none" stroke="#fff" stroke-width="1"/></svg>
        <svg class="icon" viewBox="0 0 18 18" aria-label="email"><rect width="18" height="18" fill="#33a6d7"/><rect x="3.5" y="5" width="11" height="8" fill="#fff"/><path d="M3.5 5l5.5 4.5L14.5 5" fill="none" stroke="#33a6d7" stroke-width="1.2"/></svg>
      </div>
    </div>
    <div class="address-band">418 Corvell Avenue, Unit 9 &nbsp;North Hollywood, California 91602</div>
  </section>

  <section class="card card--back" aria-label="Business card, logo side">
    <div class="wordmark"><span class="wordmark__text">Brava Set</span><span class="wordmark__dot"></span></div>
  </section>
</body>
</html>
```